Lorvika.no is a new website about pedagogical entrepreneurship. It's main target group is teachers. The Fjellmark Institute for Classroom Media and the Nordvik Agency for Schools and Study are leading the project.

The web page is meant to show examples of how different methods of entrepreneurship can be used pedagogical in a learning environment. The page will also support the user with examples of different teaching programs and other examples of best practice.

Pedagogical entrepreneurship is not about business and men in suits. It's a method for learning. The focus in the design should be on school, education and new ways of learning.

The final product should be motivating and engaging, but at the same time governmental and serious. We are not looking for something "flashy" and corporate-looking, but a moderate, task-focused and clean design that state quality.

We need designs for three pages:
1 - frontpage
2 - subpage ("Metoder og undervisningsopplegg")
3 - subpage ("Smått-VERK i Brekkelia")

The interaction design for these three pages will be uploaded as an attachment.

We would like you to find inspiration in the following websites:
- www.gryvekst.no
- www.lavrek.no
- www.tovandstudio.com
- www.kvp.no
(more will be added)

Please use the attached logo, and feel free to use this as an inspiration for the rest of the design.

Target Market(s)

Teachers

Industry/Entity Type

Education

Requirements
Must have
• * Header with: Logo. Main navigation. Utility navigation. Search box.
* Footer
Should not have
• Images of men in suits.
Very strong graphical elements that stands out too much (we want it clean).

```html
<!DOCTYPE html>
<html lang="en">
<head>
<meta charset="utf-8">
<title>Lorvika.no – Pedagogical entrepreneurship</title>
<link href="https://fonts.googleapis.com/css2?family=Arimo:wght@400;700&family=Open+Sans:ital,wght@0,400;0,700;1,400&display=swap" rel="stylesheet">
<style>
:root{
  --blue-dark:#0c4f86;
  --blue:#1a6faf;
  --blue-bright:#1b8cc8;
  --navy:#1e3a5f;
  --green:#6aa827;
  --orange:#ee6d12;
  --ink:#1a1a1a;
  --line:#c9c9c9;
  --footer-top:#0e69ad;
  --footer-bottom:#0b4f8a;
  --footer-link:#9fd6ff;
}
*{margin:0;padding:0;box-sizing:border-box}
html,body{width:1200px;height:1016px;overflow:hidden;background:#fff}
body{position:relative;font-family:"Arimo",Arial,sans-serif;color:var(--ink);font-size:12px}
a{color:var(--blue-bright)}
.abs{position:absolute}

.topbar{left:0;top:0;width:1200px;height:42px;background:linear-gradient(#1b6fae,#0d5189);color:#fff}
.topbar .welcome{left:189px;top:13px;font-size:12px}
.topbar .welcome b{font-weight:700}
.topnav{left:470px;top:13px;display:flex;font-size:12px}
.topnav span{padding:0 10px 0 12px;border-left:1px solid rgba(255,255,255,.25)}
.topnav span:first-child{border-left:0}
.topnav span::before{content:"›› ";font-size:10px}
.search{left:834px;top:9px;width:175px;height:23px;background:#0b4478;border:1px solid #2a7cbd;border-radius:2px;color:#8fb3d3;font-size:11px;padding:4px 8px}
.search svg{position:absolute;right:7px;top:5px}

.hero{left:0;top:42px;width:1200px;height:284px;background:linear-gradient(#fff 0%,#f1f1f1 45%,#d6d6d6 100%)}
.brand{left:193px;display:flex;align-items:center;gap:12px}
.brand .dot{width:44px;height:44px;border-radius:50%;background:var(--blue)}
.brand .name{font-family:"Open Sans",sans-serif;font-weight:700;font-size:42px;color:var(--blue)}
.intro{left:564px;width:448px;font-size:12.5px;line-height:15.5px}

.card{top:201px;width:270px;height:125px;background:linear-gradient(#f9f9f9,#fff);border:1px solid #ddd;border-bottom:0;border-radius:3px 3px 0 0;font-family:"Open Sans",sans-serif;padding:12px 16px}
.card .kicker{font-style:italic;font-size:14px}
.card h2{font-size:20px;line-height:22px;color:var(--navy);margin-top:3px;width:205px}
.card .bar{position:absolute;left:16px;right:16px;top:106px;height:3px;border-radius:2px}
.c1 .kicker{color:var(--blue-bright)} .c1 .bar{background:var(--blue-bright)}
.c1 h2{width:230px}
.c2 .kicker{color:var(--green)} .c2 .bar{background:var(--green)}
.c3 .kicker{color:var(--orange)} .c3 .bar{background:var(--orange)}
.shadow{left:0;top:326px;width:1200px;height:10px;background:#e5e5e5;border-top:1px solid #cfcfcf}
.shadow::after{content:"";position:absolute;left:210px;right:210px;top:0;height:12px;border-radius:0 0 50% 50%;background:radial-gradient(ellipse at top,rgba(0,0,0,.22),transparent 70%)}

.meter{left:188px;top:390px;width:270px;height:217px;background:linear-gradient(#fff,#f3f3f3);border:1px solid #d5d5d5;border-radius:3px;box-shadow:0 1px 3px rgba(0,0,0,.12);text-align:center}
.meter h3{font-weight:400;font-size:14.5px;color:var(--navy);margin-top:30px;line-height:15px}
.meter h3 b{font-weight:700}
.meter .gauge{position:absolute;left:69px;top:94px;width:132px;height:72px;background:linear-gradient(90deg,#8cc8ea,#1a6faf)}
.meter .btn{position:absolute;left:43px;top:160px;width:183px;height:29px;border:1px solid #aaa;border-radius:4px;background:linear-gradient(#fdfdfd,#dcdcdc);font-size:12px;line-height:27px;color:#222;box-shadow:0 2px 2px rgba(0,0,0,.15)}

.section-title{font-size:23px;font-weight:400;display:flex;align-items:center;gap:10px}
.section-title::after{content:"";flex:1;height:5px;background:repeating-linear-gradient(135deg,#cfcfcf 0 2px,transparent 2px 4px)}
.t-get{left:480px;top:384px;width:529px}
.t-insp{left:189px;top:635px;width:820px}

.panel{top:448px;width:254px;height:159px;border:1px solid var(--line);border-radius:3px;padding:20px 0 0 14px}
.panel h4{position:absolute;top:-14px;left:10px;background:#fff;padding:0 5px;font-weight:400;font-size:19px;color:var(--blue-bright)}
.panel ul{list-style:none}
.panel li{font-size:11.5px;line-height:20.5px}
.panel li::before{content:"››";font-size:9px;margin-right:9px}
.panel a{display:block;margin-left:16px;font-size:11.5px;margin-top:2px}
.p1{left:481px} .p2{left:754px}

.insp{left:188px;top:678px;width:820px;height:130px;border:1px solid var(--line);border-radius:3px}
.arrow{top:52px;width:24px;height:28px;background:linear-gradient(#ececec,#c9c9c9);border:1px solid #bbb}
.arrow.l{left:-1px;border-radius:0 3px 3px 0} .arrow.r{right:-1px;border-radius:3px 0 0 3px}
.arrow svg{position:absolute;left:7px;top:8px}
.item{top:26px;display:flex;gap:12px}
.item .photo{width:116px;height:78px;border:1px solid #ccc;padding:3px;background:#fff}
.item .photo div{width:100%;height:100%}
.item p{width:120px;font-size:11.5px;line-height:14px}
.item a{display:block;margin-top:12px;font-size:11.5px}
.i1{left:40px} .i2{left:294px} .i3{left:548px}

.footer{left:0;top:843px;width:1200px;height:173px;background:linear-gradient(var(--footer-top),var(--footer-bottom));color:#fff}
.footer::before{content:"";position:absolute;left:0;right:0;top:0;height:6px;background:repeating-linear-gradient(135deg,#d2d2d2 0 2px,#f4f4f4 2px 4px)}
.fcol{top:27px;font-size:11px}
.fcol h5{font-weight:400;font-size:11px;color:var(--footer-link);margin-bottom:13px}
.fcol ul{list-style:none}
.fcol li{line-height:14px;position:relative}
.fcol li::before{content:"•";position:absolute;left:-10px}
.fcol li.gap{margin-top:13px}
.fcol a{display:block;margin-top:13px;color:var(--footer-link)}
.f1{left:201px;width:150px} .f2{left:383px} .f3{left:529px} .f4{left:668px}
.fbrand{left:804px;top:28px;display:flex;align-items:center;gap:10px}
.fbrand .dot{width:40px;height:40px;border-radius:50%;background:#fff}
.fbrand .name{font-family:"Open Sans",sans-serif;font-weight:700;font-size:36px;color:#5db8f3}
.legal{right:199px;top:113px;text-align:right;font-size:10px;line-height:14px}
</style>
</head>
<body>

<header class="abs topbar">
  <div class="abs welcome">Welcome to <b>Lorvika.no</b></div>
  <nav class="abs topnav"><span>Best Practice Schools</span><span>Lorvikameter</span><span>About Lorvika.no</span></nav>
  <div class="abs search">search
    <svg width="12" height="12" viewBox="0 0 12 12"><circle cx="5" cy="5" r="3.6" fill="none" stroke="#8fb3d3" stroke-width="1.5"/><line x1="7.6" y1="7.6" x2="11" y2="11" stroke="#8fb3d3" stroke-width="1.8"/></svg>
  </div>
</header>

<section class="abs hero">
  <div class="abs brand" style="top:32px"><span class="dot"></span><span class="name">Lorvika</span></div>
  <p class="abs intro" style="top:37px">Pedagogical entrepreneurship works. Lorem ipsum dolor sit amet, consectetur adipiscing elit. Mauris quis arcu felis, eget ullamcorper augue. Pellentesque pulvinar mauris ac nunc congue feugiat. <a href="#">Learn more</a></p>
</section>

<article class="abs card c1" style="left:188px"><div class="kicker">Learn about what, why and how!</div><h2>What is pedagogical entrepreneurship?</h2><div class="bar"></div></article>
<article class="abs card c2" style="left:463px"><div class="kicker">Plan your lessons!</div><h2>Methods and teaching plans</h2><div class="bar"></div></article>
<article class="abs card c3" style="left:738px"><div class="kicker">Be inspired!</div><h2>Good example/ best practice</h2><div class="bar"></div></article>
<div class="abs shadow"></div>

<aside class="abs meter">
  <h3>ARE YOU WORKING<br><b>ENTREPRENEURSHIP-LIKE?</b></h3>
  <div class="gauge" role="img" aria-label="Blue semicircular gauge with a needle pointing to the left"></div>
  <div class="btn">TRY THE <b>LORVIKAMETER</b></div>
</aside>

<h2 class="abs section-title t-get">Get Started</h2>

<div class="abs panel p1">
  <h4>Methods</h4>
  <ul><li>Lorem ipsum dolor sit amet consectetur</li><li>Adipiscing elit ipsum dolor sit</li><li>Mauris quis acu felis eget ullamcorper</li><li>Pellentesque pulvinar mauris</li><li>Ancvac nunc congue feugiat</li></ul>
  <a href="#">See more</a>
</div>
<div class="abs panel p2">
  <h4>Teaching Plans</h4>
  <ul><li>Lorem ipsum dolor sit amet consectetur</li><li>Adipiscing elit ipsum dolor sit</li><li>Mauris quis acu felis eget ullamcorper</li><li>Pellentesque pulvinar mauris</li><li>Ancvac nunc congue feugiat</li></ul>
  <a href="#">See more</a>
</div>

<h2 class="abs section-title t-insp">Inspiration</h2>

<div class="abs insp">
  <div class="abs arrow l"><svg width="8" height="12" viewBox="0 0 8 12"><path d="M7 1 L2 6 L7 11" fill="none" stroke="#666" stroke-width="2.5"/></svg></div>
  <div class="abs item i1"><div class="photo"><div role="img" aria-label="Teachers smiling together at a meeting table" style="background:linear-gradient(90deg,#c89a80,#e9e2da 60%,#f4f4f4)"></div></div><div><p>Lorem ipsum dolor sit amet adipiscing elit ipsum dolor sit mauris felis eget ullamcorper</p><a href="#">more</a></div></div>
  <div class="abs item i2"><div class="photo"><div role="img" aria-label="Teacher standing in front of library bookshelves" style="background:linear-gradient(90deg,#6b4a2c,#2a2a2a 50%,#8a5a34)"></div></div><div><p>Lorem ipsum dolor sit amet adipiscing elit ipsum dolor sit mauris felis eget ullamcorper</p><a href="#">more</a></div></div>
  <div class="abs item i3"><div class="photo"><div role="img" aria-label="Student in pink top standing by colourful bookshelves" style="background:linear-gradient(90deg,#5a6f8a,#d4468c 50%,#6a7b92)"></div></div><div><p>Lorem ipsum dolor sit amet adipiscing elit ipsum dolor sit mauris felis eget ullamcorper</p><a href="#">more</a></div></div>
  <div class="abs arrow r"><svg width="8" height="12" viewBox="0 0 8 12"><path d="M1 1 L6 6 L1 11" fill="none" stroke="#666" stroke-width="2.5"/></svg></div>
</div>

<footer class="abs footer">
  <div class="abs fcol f1"><h5>Pedagogical Entrepreneurship</h5><ul><li>What is Pedagogical Entrepreneurship?</li><li>Science</li><li>Best practice schools</li><li>Lorvikameter</li><li class="gap">About lorvika.no</li></ul></div>
  <div class="abs fcol f2"><h5>Methods</h5><ul><li>Lorem ipsum dolor</li><li>Sit amet adipiscing</li><li>Elit ipsum dolor sit</li><li>Mauris felis eget</li></ul><a href="#">See more</a></div>
  <div class="abs fcol f3"><h5>Teaching Plans</h5><ul><li>Lorem ipsum dolor</li><li>Sit amet adipiscing</li><li>Elit ipsum dolor sit</li><li>Mauris felis eget</li></ul><a href="#">See more</a></div>
  <div class="abs fcol f4"><h5>Gode Eksempler</h5><ul><li>Lorem ipsum dolor</li><li>Sit amet adipiscing</li><li>Elit ipsum dolor sit</li><li>Mauris felis eget</li></ul><a href="#">See more</a></div>
  <div class="abs fbrand"><span class="dot"></span><span class="name">Lorvika</span></div>
  <div class="abs legal">© 2012 lorvika.no &nbsp;.&nbsp; All rights reserved<br>Terms of use &nbsp;.&nbsp; Privacy Policy</div>
</footer>

</body>
</html>
```